Corrow Family Farm fresh honey jar label

I need a label for jars of honey harvested at our farm. These are for gifts and personal use. We are looking to incorporate our farm brand into the label. We would like the design to take the existing brand and add some element like bees, honey, flowers, or hives to indicate the contents. We want the design to feel homemade and authentic without feeling cheap or hoaky

Requirements
Must have
• The label must be made to fit a 1" x2" rectangular label. The label must include the attached family brand. The label must include the text "Corrow Family Farms" "Pinebrook, USA" "Farm Fresh Honey". The label will be printed on off-white paper
Nice to have
• It would be nice to have illustrations of bees or flowers around the logo or hives or honeycombs. The label should have a vintage feel
Should not have
• The label should not feel overly cartoonish or hoaky

```html
<!DOCTYPE html>
<html lang="en">
<head>
<meta charset="UTF-8">
<title>Corrow Family Farms – Farm Fresh Honey Label</title>
<link href="https://fonts.googleapis.com/css2?family=Cinzel:wght@600&family=Roboto+Condensed:wght@400;500&display=swap" rel="stylesheet">
<style>
  :root {
    --page: #ffffff;
    --paper: #ebe8dc;
    --frame: #e0a93a;
    --title-brown: #5b4316;
    --ink: #2b2a26;
    --comb-yellow: #d9c63a;
    --comb-light: #e8df9a;
  }
  html, body {
    margin: 0;
    padding: 0;
    width: 1200px;
    height: 870px;
    overflow: hidden;
    background: var(--page);
  }
  .canvas {
    position: relative;
    width: 1200px;
    height: 870px;
  }
  .label {
    position: absolute;
    left: 400px;
    top: 35px;
    width: 400px;
    height: 800px;
    background: var(--paper);
    border-radius: 28px;
  }
  .label__frame {
    position: absolute;
    inset: 22px;
    border: 2px solid var(--frame);
    border-radius: 20px;
  }
  .brand-mark {
    position: absolute;
    top: 58px;
    left: 0;
    right: 0;
    text-align: center;
    font-family: "Roboto Condensed", sans-serif;
    font-weight: 500;
    font-size: 22px;
    line-height: 1.1;
    letter-spacing: 1px;
    color: var(--ink);
  }
  .product-title {
    position: absolute;
    top: 145px;
    left: 0;
    right: 0;
    margin: 0;
    text-align: center;
    font-family: "Cinzel", serif;
    font-weight: 600;
    color: var(--title-brown);
    line-height: 0.92;
  }
  .product-title span { display: block; }
  .product-title .t-farm { font-size: 70px; }
  .product-title .t-fresh { font-size: 88px; }
  .product-title .t-honey { font-size: 76px; }
  .comb-art {
    position: absolute;
    left: 45px;
    top: 395px;
    width: 305px;
    height: 165px;
    border-radius: 14px;
    background: radial-gradient(ellipse at 55% 45%, var(--comb-yellow) 0%, var(--comb-yellow) 35%, var(--comb-light) 62%, var(--paper) 100%);
  }
  .divider {
    position: absolute;
    top: 593px;
    left: 150px;
    width: 100px;
    height: 2px;
    background: var(--frame);
  }
  .farm-name {
    position: absolute;
    top: 615px;
    left: 0;
    right: 0;
    margin: 0;
    text-align: center;
    font-family: "Roboto Condensed", sans-serif;
    font-weight: 400;
    font-size: 39px;
    line-height: 1.12;
    color: var(--ink);
  }
  .farm-location {
    position: absolute;
    top: 730px;
    left: 0;
    right: 0;
    margin: 0;
    text-align: center;
    font-family: "Roboto Condensed", sans-serif;
    font-weight: 500;
    font-size: 24px;
    color: var(--ink);
  }
</style>
</head>
<body>
<main class="canvas">
  <section class="label">
    <div class="label__frame"></div>
    <div class="brand-mark">CORROW<br>FAMILY FARM</div>
    <h1 class="product-title">
      <span class="t-farm">FARM</span>
      <span class="t-fresh">FRESH</span>
      <span class="t-honey">HONEY</span>
    </h1>
    <div class="comb-art" role="img" aria-label="Illustration of a golden honeycomb with two small bees and dashed flight paths"></div>
    <div class="divider"></div>
    <p class="farm-name">CORROW FAMILY<br>FARMS</p>
    <p class="farm-location">PINEBROOK, USA</p>
  </section>
</main>
</body>
</html>
```